Let Us Bloom speaking engagement

the flyer is about a speaking engagement for women's groups. Flyer should be simple, soft, engaging, clean and professional. I am a life coach and also a talk show host. the event I will be advertising is for groups of women. It will be given to church groups, female clubs and organizations. The name of my company is Mara's Lantern Life Coaching Institute.

Target Market(s)

professional women over thirty years old

Font styles to use
Script

Colors
ffffff
34a7d8
85cae6

Requirements
Must have
• use my photo and logo only
Should not have
• anything distracting

```html
<!DOCTYPE html>
<html lang="en">
<head>
<meta charset="utf-8">
<title>Let Us Bloom – Speaking Engagement Flyer</title>
<link rel="stylesheet" href="https://fonts.googleapis.com/css2?family=Oswald:wght@500;600;700&family=Montserrat:wght@500;600;700&display=swap">
<style>
  :root {
    --white: #ffffff;
    --sky: #34a7d8;
    --sky-soft: #85cae6;
    --sky-deep: #1f93cf;
    --ink: #3d3d3f;
    --ink-dark: #1c2633;
    --stage: #e6e6e6;
  }
  * { box-sizing: border-box; margin: 0; padding: 0; }
  html, body { width: 1200px; height: 1200px; overflow: hidden; }
  body {
    background: var(--stage);
    position: relative;
    font-family: "Montserrat", sans-serif;
  }
  .flyer {
    position: absolute;
    left: 244px;
    top: 101px;
    width: 712px;
    height: 998px;
    background: var(--white);
    overflow: hidden;
  }
  .flyer-shapes { position: absolute; inset: 0; }
  .logo-placeholder {
    position: absolute;
    left: 44px;
    top: 38px;
    font-family: "Oswald", sans-serif;
    font-weight: 700;
    font-size: 82px;
    line-height: 72px;
    color: var(--ink);
  }
  .headline {
    position: absolute;
    left: 34px;
    top: 246px;
    font-family: "Oswald", sans-serif;
    font-weight: 600;
    font-size: 60px;
    line-height: 54px;
    color: var(--sky);
  }
  .headline-tag {
    position: absolute;
    left: 34px;
    top: 366px;
    width: 261px;
    height: 51px;
    background: var(--sky-soft);
    color: var(--white);
    font-weight: 600;
    font-size: 36px;
    line-height: 51px;
    text-align: center;
  }
  .coach-intro {
    position: absolute;
    left: 36px;
    top: 426px;
    font-weight: 500;
    font-size: 30px;
    color: var(--ink);
  }
  .coach-name {
    position: absolute;
    left: 38px;
    top: 466px;
    font-family: "Oswald", sans-serif;
    font-weight: 700;
    font-size: 49px;
    line-height: 56px;
    color: var(--sky-deep);
  }
  .session-blurb {
    position: absolute;
    right: 27px;
    top: 601px;
    text-align: right;
    white-space: nowrap;
    font-weight: 500;
    font-size: 20px;
    line-height: 25.6px;
    color: var(--white);
  }
  .invite-label {
    position: absolute;
    left: 436px;
    top: 716px;
    width: 248px;
    height: 50px;
    background: var(--white);
    color: var(--sky-deep);
    font-weight: 700;
    font-size: 40px;
    line-height: 50px;
    text-align: right;
    padding-right: 8px;
    letter-spacing: 1px;
  }
  .invite-name {
    position: absolute;
    right: 28px;
    top: 776px;
    font-family: "Oswald", sans-serif;
    font-weight: 700;
    font-size: 64px;
    line-height: 80px;
    color: var(--white);
    letter-spacing: 2px;
    text-shadow: 2px 3px 4px rgba(0, 40, 80, 0.45);
  }
  .invite-audience {
    position: absolute;
    right: 28px;
    top: 864px;
    text-align: right;
    font-weight: 600;
    font-size: 20px;
    line-height: 25px;
    color: var(--white);
  }
  .contact-line {
    position: absolute;
    right: 24px;
    top: 944px;
    display: flex;
    align-items: center;
    gap: 10px;
    font-family: "Oswald", sans-serif;
    font-weight: 600;
    font-size: 22px;
    line-height: 36px;
    color: var(--ink-dark);
  }
  .contact-line svg { width: 22px; height: 22px; }
</style>
</head>
<body>
  <main class="flyer">
    <svg class="flyer-shapes" width="712" height="998" viewBox="0 0 712 998" xmlns="http://www.w3.org/2000/svg">
      <defs>
        <linearGradient id="portraitTone" x1="0" y1="0" x2="1" y2="1">
          <stop offset="0" stop-color="#5a4a3a"/>
          <stop offset="0.5" stop-color="#7a5a44"/>
          <stop offset="1" stop-color="#3b2c22"/>
        </linearGradient>
        <linearGradient id="panelTone" x1="1" y1="0" x2="0" y2="1">
          <stop offset="0" stop-color="#1288c8"/>
          <stop offset="1" stop-color="#44aee0"/>
        </linearGradient>
        <linearGradient id="loungeTone" x1="0" y1="0" x2="0" y2="1">
          <stop offset="0" stop-color="#34407c"/>
          <stop offset="1" stop-color="#3550a8"/>
        </linearGradient>
      </defs>

      <rect class="contact-band" x="0" y="928" width="712" height="70" fill="var(--sky-soft)"/>

      <polygon class="info-panel" points="252,556 712,556 712,924 250,924 92,766" fill="url(#panelTone)"/>

      <polygon class="accent-triangle" points="318,556 382,470 450,556" fill="#4fb3df"/>
      <polygon class="accent-triangle-light" points="382,470 450,556 410,556" fill="#7cc6e8"/>

      <polyline class="chevron-line" points="198,595 38,768 128,872" fill="none" stroke="#6cbde4" stroke-width="3.5"/>
      <polyline class="chevron-line" points="220,605 64,768 150,866" fill="none" stroke="#6cbde4" stroke-width="3.5"/>

      <polygon class="portrait-main" role="img" aria-label="Portrait photo of the life coach smiling" points="396,0 712,0 712,568 456,568 262,284" fill="url(#portraitTone)"/>

      <rect class="portrait-lounge" role="img" aria-label="Photo of the life coach relaxing on a sofa in a blue top" x="0" y="717" width="392" height="281" fill="url(#loungeTone)"/>
    </svg>

    <div class="logo-placeholder">YOUR<br>LOGO</div>

    <h1 class="headline">A HEART<br>TO HEART</h1>
    <div class="headline-tag">conversation</div>
    <p class="coach-intro">with Life Coach</p>
    <p class="coach-name">NADIRA COLE</p>

    <p class="session-blurb">Let Us Bloom is an interactive soul search-<br>ing session that will help women share<br>their stories and be real about the things<br>that matter most</p>

    <div class="invite-label">TO INVITE</div>
    <p class="invite-name">NADIRA</p>
    <p class="invite-audience">to your women's group<br>or gathering</p>

    <p class="contact-line">242-555-0148 OR 555-0192
      <svg viewBox="0 0 24 24" aria-hidden="true">
        <path d="M6.6 3.5 L9.2 6.8 L7.6 8.6 Q9 12.6 12.8 15 L14.6 13.4 L18 16 L16.4 19.2 Q10.6 19.6 6.4 14 Q3 9.4 4 5.2 Z" fill="var(--sky-deep)"/>
        <path d="M14 4 A6 6 0 0 1 20 10" fill="none" stroke="var(--sky-deep)" stroke-width="1.8" stroke-linecap="round"/>
        <path d="M14 7.4 A2.8 2.8 0 0 1 16.6 10" fill="none" stroke="var(--sky-deep)" stroke-width="1.8" stroke-linecap="round"/>
      </svg>
    </p>
  </main>
</body>
</html>
```